Upscale business cards needed for family office

We would like professional business cards created for employees of our family office. Relatively simple and straightforward, but also with a unique element to set them apart. Probably stick with neutral and simple colors that mesh well with the colors in the logo. We need space for the traditional elements, including name, title, address, email/phone number.

Industry/Entity Type

Business

Contact Information for Business Card

Space for name, title, phone number, email, address

```html
<!DOCTYPE html>
<html lang="en">
<head>
<meta charset="utf-8">
<title>Larkmoor Business Cards</title>
<link rel="stylesheet" href="https://fonts.googleapis.com/css2?family=Arimo:wght@400;700&display=swap">
<style>
  :root {
    --backdrop: #2e2724;
    --card: #141414;
    --card-edge: #1f1f1f;
    --ink: #f2f2f2;
    --muted: #c9ccce;
    --accent: #1d9ccf;
  }
  * { margin: 0; padding: 0; box-sizing: border-box; }
  html, body {
    width: 1200px; height: 780px; overflow: hidden;
    background: var(--backdrop);
    font-family: "Arimo", Arial, sans-serif;
  }
  .canvas {
    position: relative; width: 1200px; height: 780px;
    display: flex; align-items: center; justify-content: center; gap: 60px;
  }
  .card {
    position: relative; width: 520px; height: 300px;
    background: var(--card);
    border: 1px solid var(--card-edge);
    border-radius: 4px;
    box-shadow: 0 14px 30px rgba(0,0,0,0.45);
  }
  .brand {
    position: absolute; display: flex; align-items: center; gap: 12px;
    color: var(--muted); font-weight: 400; letter-spacing: 0.02em;
  }
  .brand-square { width: 22px; height: 22px; background: var(--accent); }
  .card-front .brand { left: 50%; top: 50%; transform: translate(-50%, -50%); font-size: 38px; }
  .card-back .brand { left: 270px; top: 58px; transform: translateX(-50%); font-size: 32px; }
  .person {
    position: absolute; right: 290px; top: 176px; text-align: right;
  }
  .person-name { color: var(--ink); font-size: 24px; line-height: 1.1; }
  .person-title { color: var(--accent); font-size: 17px; margin-top: 4px; }
  .divider {
    position: absolute; left: 250px; top: 160px; width: 2px; height: 100px;
    background: var(--accent);
  }
  .contacts {
    position: absolute; left: 270px; top: 172px; list-style: none;
    color: var(--ink); font-size: 16px;
  }
  .contacts li { display: flex; align-items: center; gap: 10px; height: 26px; }
  .contact-icon { width: 16px; height: 16px; flex: none; }
</style>
</head>
<body>
<main class="canvas">
  <section class="card card-front">
    <div class="brand"><span class="brand-square"></span><span class="brand-name">Larkmoor</span></div>
  </section>

  <section class="card card-back">
    <div class="brand"><span class="brand-square"></span><span class="brand-name">Larkmoor</span></div>
    <div class="person">
      <p class="person-name">Evan Corder</p>
      <p class="person-title">Managing Director</p>
    </div>
    <div class="divider"></div>
    <ul class="contacts">
      <li>
        <svg class="contact-icon" viewBox="0 0 16 16" aria-hidden="true"><rect width="16" height="16" rx="2" fill="#1d9ccf"/><path d="M5 3.5c-1 .6-1.4 1.8-.8 3.3.8 2.1 2.9 4.4 5 5.3 1.4.6 2.6.2 3.3-.8l-1.7-1.6-1.3.7C8.3 9.8 6.8 8.3 6.2 7l.7-1.3z" fill="#141414"/></svg>
        <span>021-555-0137</span>
      </li>
      <li>
        <svg class="contact-icon" viewBox="0 0 16 16" aria-hidden="true"><rect width="16" height="16" rx="2" fill="#1d9ccf"/><rect x="3" y="4.5" width="10" height="7" fill="#141414"/><path d="M3 4.5l5 4 5-4" fill="none" stroke="#1d9ccf" stroke-width="1"/></svg>
        <span>evan@larkmoor.com</span>
      </li>
      <li>
        <svg class="contact-icon" viewBox="0 0 16 16" aria-hidden="true"><rect width="16" height="16" rx="2" fill="#1d9ccf"/><path d="M8 2.8a3.6 3.6 0 0 0-3.6 3.6c0 2.6 3.6 6.8 3.6 6.8s3.6-4.2 3.6-6.8A3.6 3.6 0 0 0 8 2.8z" fill="#141414"/><circle cx="8" cy="6.4" r="1.3" fill="#1d9ccf"/></svg>
        <span>480 W Linden Rd</span>
      </li>
    </ul>
  </section>
</main>
</body>
</html>
```